Professional and Fun Business Cards for #1 Lagoon Care

We want an updated look for our existing business cards. In addition, we need to update the logos on the back side of the card to be the most current award for Brevin's Ledger. I have an eps of the Brevin's Ledger award logo but it is too big to upload here, so I can email it to the designer once selected.

Target Market(s)

Families with swimming pools

Industry/Entity Type

Business

Contact Information for Business Card

Thomas Garvey
Partner & Senior Pool Technician
Garvey & Kin Pool Service, Inc.
2460 Marlow Avenue, Suite 310
Brightwater, CA 95000
(916) 555-0143 service
(916) 555-0187 billing
info@garvey-kin.example
www.garvey-kin.example

Font styles to use
Other font styles liked:
• Goudy Sans Bold

Colors
3176b5
34a7d8
34b8a4
add136

Requirements
Must have
• Garvey & Kin logo and contact information on the front
• All other logos on the back
Nice to have
• Open to ideas...
Should not have
• Can't think of anything specific

```html
<!DOCTYPE html>
<html lang="en">
<head>
<meta charset="utf-8">
<title>Garvey &amp; Kin Pool Service – Business Cards</title>
<link rel="stylesheet" href="https://fonts.googleapis.com/css2?family=Alegreya+Sans:wght@500;700&display=swap">
<style>
  :root {
    --teal: #4fcfc2;
    --teal-deep: #34b8a4;
    --brand-blue: #3176b5;
    --sky: #34a7d8;
    --paper: #ffffff;
    --backdrop: #e9ecec;
    --ink-light: #ffffff;
  }
  * { box-sizing: border-box; margin: 0; padding: 0; }
  html, body {
    width: 1200px; height: 885px; overflow: hidden;
    background: var(--backdrop);
    font-family: "Alegreya Sans", sans-serif;
  }
  .canvas { position: relative; width: 1200px; height: 885px; }
  .card {
    position: absolute; width: 640px; height: 366px;
    background: var(--paper);
    box-shadow: 0 6px 18px rgba(0,0,0,0.18);
    overflow: hidden;
  }
  .card--front { left: 120px; top: 45px; display: flex; }
  .card--back { left: 440px; top: 474px; }

  .front__info {
    width: 54%; height: 100%;
    background: linear-gradient(160deg, #63ddd1 0%, var(--teal) 45%, var(--teal-deep) 100%);
    color: var(--ink-light);
    padding: 34px 28px 0 34px;
  }
  .company { font-size: 21px; font-weight: 700; line-height: 1.1; }
  .person { margin-top: 20px; font-size: 19px; font-weight: 700; }
  .role { font-size: 14px; font-weight: 500; margin-top: 2px; }
  .contacts { margin-top: 22px; list-style: none; font-size: 15px; font-weight: 500; }
  .contacts li { display: flex; align-items: flex-start; gap: 10px; line-height: 1.25; margin-bottom: 5px; }
  .contacts svg { flex: 0 0 16px; width: 16px; height: 16px; margin-top: 2px; }

  .front__brand { width: 46%; display: flex; align-items: center; justify-content: center; }
  .brand {
    display: flex; align-items: center; gap: 10px;
    color: var(--brand-blue); font-weight: 700; font-size: 32px;
  }
  .brand__mark { width: 22px; height: 22px; background: var(--brand-blue); }

  .back__band { position: absolute; left: 0; right: 0; height: 26px; background: var(--teal-deep); }
  .back__band--top { top: 0; }
  .back__band--bottom { bottom: 0; }
  .card--back .brand {
    position: absolute; left: 0; right: 0; top: 0; bottom: 0;
    justify-content: center; font-size: 38px;
  }
</style>
</head>
<body>
<div class="canvas">
  <section class="card card--front">
    <div class="front__info">
      <p class="company">Garvey &amp; Kin Pool Service, Inc.</p>
      <p class="person">Thomas Garvey</p>
      <p class="role">Partner &amp; Senior Pool Technician</p>
      <ul class="contacts">
        <li>
          <svg viewBox="0 0 16 16" fill="none" stroke="#fff" stroke-width="1.4"><path d="M4 2h2.5l1 3-1.6 1.2a8 8 0 0 0 3.9 3.9L11 8.5l3 1V12a2 2 0 0 1-2 2A10 10 0 0 1 2 4a2 2 0 0 1 2-2z"/></svg>
          <span>(916) 555-0143</span>
        </li>
        <li>
          <svg viewBox="0 0 16 16" fill="none" stroke="#fff" stroke-width="1.4"><rect x="4.5" y="1.5" width="7" height="13" rx="1.2"/><line x1="7" y1="12.3" x2="9" y2="12.3"/></svg>
          <span>(916) 555-0187</span>
        </li>
        <li>
          <svg viewBox="0 0 16 16" fill="none" stroke="#fff" stroke-width="1.4"><rect x="1.5" y="3.5" width="13" height="9" rx="1"/><path d="M1.5 4l6.5 5 6.5-5"/></svg>
          <span>info@garvey-kin.example</span>
        </li>
        <li>
          <svg viewBox="0 0 16 16" fill="none" stroke="#fff" stroke-width="1.3"><circle cx="8" cy="8" r="6.5"/><ellipse cx="8" cy="8" rx="2.8" ry="6.5"/><line x1="1.5" y1="8" x2="14.5" y2="8"/></svg>
          <span>www.garvey-kin.example</span>
        </li>
        <li>
          <svg viewBox="0 0 16 16" fill="none" stroke="#fff" stroke-width="1.4"><path d="M8 15s5-5 5-8.5A5 5 0 0 0 3 6.5C3 10 8 15 8 15z"/><circle cx="8" cy="6.5" r="1.8"/></svg>
          <span>2460 Marlow Avenue, Suite 310 Brightwater<br>CA 95000</span>
        </li>
      </ul>
    </div>
    <div class="front__brand">
      <div class="brand"><span class="brand__mark"></span><span>Garvey &amp; Kin</span></div>
    </div>
  </section>

  <section class="card card--back">
    <div class="back__band back__band--top"></div>
    <div class="brand"><span class="brand__mark"></span><span>Garvey &amp; Kin</span></div>
    <div class="back__band back__band--bottom"></div>
  </section>
</div>
</body>
</html>
```